Tenlo business card

I'm a hack at Illustrator, but have put together a set of business cards as attached. If someone could please improve these including good font selection, standard font sizes and spacing, nice layout and symmetry. Rear side the same on all cards. Basically make these cards into something impressive and professional.
Updates

Official logo just uploaded, please use these colours

Target Market(s)

50+ year old married couples

Industry/Entity Type

Business

Requirements
Must have
• Professional
Should not have
• Silly, cartoony

```html
<!DOCTYPE html>
<html lang="en">
<head>
<meta charset="utf-8">
<title>Tenlo business card</title>
<link rel="stylesheet" href="https://fonts.googleapis.com/css2?family=Ubuntu:wght@500;700&family=Mulish:wght@400;800&display=swap">
<style>
  :root {
    --stage: #717070;
    --card: #ffffff;
    --teal: #0f6b7b;
    --ink: #2b3a3f;
    --text: #2a2a2a;
  }
  * { margin: 0; padding: 0; box-sizing: border-box; }
  html, body { width: 1200px; height: 1096px; overflow: hidden; background: var(--stage); }
  .canvas { position: relative; width: 1200px; height: 1096px; }
  .card { position: absolute; left: 197px; width: 805px; height: 458px; background: var(--card); overflow: hidden; }
  .card--front { top: 54px; }
  .card--back { top: 556px; }
  .card__band { position: absolute; left: 0; bottom: 0; width: 100%; height: 16px; background: var(--teal); }

  .brand { position: absolute; text-align: center; }
  .brand__rule { display: block; height: 0; border-top: 3px solid var(--ink); }
  .brand__name { font-family: "Mulish", sans-serif; font-weight: 800; color: var(--teal); line-height: 1; white-space: nowrap; }
  .brand__tagline { font-family: "Mulish", sans-serif; font-weight: 400; color: var(--ink); line-height: 1; white-space: nowrap; }

  .card--front .brand { left: 231px; top: 271px; width: 344px; }
  .card--front .brand__name { font-size: 56px; letter-spacing: 40px; margin-top: 18px; margin-right: -40px; }
  .card--front .brand__tagline { font-size: 19px; letter-spacing: 3.4px; margin-top: 10px; margin-right: -3.4px; }

  .card--back .brand { left: 86px; top: 254px; width: 215px; }
  .card--back .brand__rule { border-top-width: 2px; }
  .card--back .brand__name { font-size: 33px; letter-spacing: 24px; margin-top: 12px; margin-right: -24px; }
  .card--back .brand__tagline { font-size: 12px; letter-spacing: 2.2px; margin-top: 6px; margin-right: -2.2px; }

  .contact { position: absolute; left: 383px; top: 70px; width: 422px; font-family: "Mulish", sans-serif; color: var(--text); }
  .contact__name { font-family: "Ubuntu", sans-serif; font-weight: 700; font-size: 28px; color: var(--teal); line-height: 32px; }
  .contact__role { font-family: "Ubuntu", sans-serif; font-weight: 500; font-size: 18px; line-height: 20px; margin-top: 4px; }
  .contact__line { font-size: 18px; line-height: 24.3px; }
  .contact__divider { height: 0; border-top: 1px solid var(--teal); margin: 6px 0 12px; }
  .contact__web { color: var(--teal); }
  .contact__gap { display: inline-block; width: 14px; }
</style>
</head>
<body>
<main class="canvas">
  <section class="card card--front">
    <div class="brand">
      <span class="brand__rule"></span>
      <p class="brand__name">TENLO</p>
      <p class="brand__tagline">BUILT FOR BETTER LIVING</p>
    </div>
    <div class="card__band"></div>
  </section>

  <section class="card card--back">
    <div class="brand">
      <span class="brand__rule"></span>
      <p class="brand__name">TENLO</p>
      <p class="brand__tagline">BUILT FOR BETTER LIVING</p>
    </div>
    <div class="contact">
      <p class="contact__name">Grant Hollis</p>
      <p class="contact__role">General Manager</p>
      <p class="contact__line">Building &amp; Technology Innovator</p>
      <div class="contact__divider"></div>
      <p class="contact__line">M: 0412 555 301</p>
      <p class="contact__line">D: 03 9555 2140</p>
      <p class="contact__line">grant.hollis@tenlo.com.au</p>
      <div class="contact__divider"></div>
      <p class="contact__line">8/41 Harlow St</p>
      <p class="contact__line">Elmvale, VIC 3199, Australia</p>
      <p class="contact__line">Ph: (+61) 03 9555 2100</p>
      <p class="contact__line contact__web">www.tenlo.com.au</p>
      <p class="contact__line">REC 30415<span class="contact__gap"></span>ABN XXXXXXXXXXXXXX</p>
    </div>
    <div class="card__band"></div>
  </section>
</main>
</body>
</html>
```